Info Graphic about Maple Orchard Restaurant

This info graphic should detail all releavent details about Maple Orchard, such as opening hours, accepted payment methods, home delivery areas etc. please refer attached word document for details.

Also attached a pdf with old info graphic.

IMPORTANT:. Given there is lot of text, I expect the designer to make this interesting. This will be printed in A1 and also A4
Also, I need this in both Portrait and landscape designs.

Industry/Entity Type

Hospitality

Font styles to use
Serif
Sans Serif
Decorative
Script
Other font styles liked:
• I let designer choose

Colors

Designer to choose colors to be used in the design.

Requirements
Must have
• Refer attached word doc
Nice to have
• Refer attached word doc
Should not have
• Refer attached word doc

```html
<!DOCTYPE html>
<html lang="en">
<head>
<meta charset="utf-8">
<title>Maple Orchard Indian Restaurant – Guest Information</title>
<link rel="stylesheet" href="https://fonts.googleapis.com/css2?family=Roboto:wght@400;700&family=Fira+Sans:wght@300;400&display=swap">
<style>
  :root {
    --ink-dark: #0d0d0d;
    --bg-mid: #1e211f;
    --heading: #f4e81c;
    --text: #ffffff;
    --brand-red: #c4101b;
    --alert-red: #ff0016;
    --paper: #ffffff;
  }
  * { margin: 0; padding: 0; box-sizing: border-box; }
  html, body { width: 849px; height: 1200px; overflow: hidden; background: var(--ink-dark); }
  .sheet {
    position: relative; width: 849px; height: 1200px; overflow: hidden;
    font-family: "Fira Sans", sans-serif; color: var(--text);
  }
  .backdrop {
    position: absolute; inset: 0;
    background: radial-gradient(ellipse at 55% 50%, #2a2e2b 0%, var(--bg-mid) 35%, var(--ink-dark) 85%);
  }
  .masthead {
    position: absolute; left: 0; top: 0; width: 849px; height: 161px;
    background: var(--paper); border-radius: 0 0 95px 95px;
  }
  .brand-mark {
    position: absolute; left: 96px; top: 50px; width: 58px; height: 58px;
    border-radius: 50%; background: var(--brand-red);
  }
  .brand-name {
    position: absolute; left: 178px; top: 54px;
    font-family: "Roboto", sans-serif; font-weight: 700; font-size: 40px; line-height: 50px;
    color: var(--brand-red); white-space: nowrap;
  }
  .section { position: absolute; }
  .section.left { left: 53px; }
  .section.right { right: 54px; text-align: right; }
  .section h2 {
    font-family: "Roboto", sans-serif; font-weight: 400; font-size: 31px; line-height: 36px;
    color: var(--heading); white-space: nowrap;
  }
  .section p, .section li { font-size: 15px; line-height: 20.4px; font-weight: 300; white-space: nowrap; }
  .label { color: var(--heading); }
  .management { top: 211px; }
  .management dl { display: grid; grid-template-columns: 77px auto; margin-top: 13px; row-gap: 6px; font-size: 19px; line-height: 22px; }
  .payment { top: 379px; }
  .payment p:first-of-type { margin-top: 17px; }
  .booking { top: 531px; }
  .booking p:first-of-type { margin-top: 16px; }
  .delivery { top: 662px; }
  .delivery .intro { margin-top: 15px; }
  .suburbs { display: grid; grid-template-columns: 149px auto; margin-top: 20px; }
  .suburbs ol { list-style: none; }
  .suburbs li { display: grid; grid-template-columns: 33px auto; }
  .delivery .fee { margin-top: 20px; }
  .rules { top: 936px; }
  .rules p:first-of-type { margin-top: 16px; }
  .registration { top: 211px; }
  .registration .company { margin-top: 15px; font-size: 17px; line-height: 22px; letter-spacing: -0.4px; }
  .registration dl { display: grid; grid-template-columns: auto auto; justify-content: end; column-gap: 12px; margin-top: 13px; font-size: 18.5px; line-height: 24.4px; }
  .registration dd { text-align: right; }
  .registration dt { color: var(--heading); text-align: right; }
  .vouchers { top: 457px; }
  .vouchers p:first-of-type { margin-top: 16px; }
  .byo { top: 604px; }
  .byo p:first-of-type { margin-top: 15px; }
  .online { top: 731px; }
  .online p:first-of-type { margin-top: 14px; }
  .facilities { top: 892px; }
  .facilities p:first-of-type { margin-top: 14px; }
  .facilities p { line-height: 20.8px; }
  .alert-band {
    position: absolute; left: 0; top: 1071px; width: 849px; height: 129px;
    background: var(--alert-red); border-radius: 95px 95px 0 0; text-align: center;
  }
  .alert-band h3 {
    margin-top: 29px; font-family: "Roboto", sans-serif; font-weight: 400;
    font-size: 29px; line-height: 32px; letter-spacing: 8px; padding-left: 8px;
  }
  .alert-band p { margin-top: 3px; font-size: 17.5px; line-height: 22px; }
</style>
</head>
<body>
<main class="sheet">
  <div class="backdrop" role="img" aria-label="Dark background photograph of spice bowls and dishes on a table"></div>

  <header class="masthead">
    <span class="brand-mark"></span>
    <h1 class="brand-name">Maple Orchard Indian Restaurant</h1>
  </header>

  <section class="section left management">
    <h2>New Management</h2>
    <dl>
      <dt class="label">Owner</dt><dd>Asha Verma</dd>
      <dt class="label">Mobile</dt><dd>0400111222</dd>
      <dt class="label">Email</dt><dd>asha@mapleorchard.com.au</dd>
    </dl>
  </section>

  <section class="section left payment">
    <h2>Payment Methods</h2>
    <p>We accept cash, all Australian EFTPOS, Debit and Credit Cards.</p>
    <p>We accept Orbix, Kestrel – A surcharge of 2.8% apply.</p>
    <p>We DO NOT accept Vantage Card</p>
  </section>

  <section class="section left booking">
    <h2>Book your Table</h2>
    <p>Please visit www.mapleorchard.com.au to book your table</p>
    <p>or contact us on 08 9000 1234</p>
  </section>

  <section class="section left delivery">
    <h2>Home/Office Delivery</h2>
    <p class="intro">We deliver to following suburbs</p>
    <div class="suburbs">
      <ol>
        <li><span>1.</span><span>Fernvale</span></li>
        <li><span>2.</span><span>Ashbury</span></li>
        <li><span>3.</span><span>X</span></li>
        <li><span>4.</span><span>X</span></li>
        <li><span>5.</span><span>X</span></li>
      </ol>
      <ol>
        <li><span>6.</span><span>X</span></li>
        <li><span>7.</span><span>X</span></li>
        <li><span>8.</span><span>X</span></li>
        <li><span>9.</span><span>X</span></li>
        <li><span>10.</span><span>X</span></li>
      </ol>
    </div>
    <p class="fee">Delivery Charges $5 and minimum order value $30</p>
  </section>

  <section class="section left rules">
    <h2>House Rules</h2>
    <p>Prices are inclusive of GST</p>
    <p>Prices are subject to change without notice</p>
    <p>Outside Food and Beverages (except WINE) are not allowed</p>
  </section>

  <section class="section right registration">
    <h2>Registration Details</h2>
    <p class="company">Birchwood Holdings Pty Ltd T/A Maple Orchard Restaurant</p>
    <dl>
      <dd>12 345 678 901</dd><dt>ABN</dt>
      <dd>Shop 4-5, 210 Larchmont Avenue,<br>Fernvale, WA 6099</dd><dt></dt>
      <dd>08 9000 1234</dd><dt>Ph</dt>
      <dd>admin@mapleorchard.com.au</dd><dt>Email</dt>
    </dl>
  </section>

  <section class="section right vouchers">
    <h2>Discount Vouchers</h2>
    <p>We accept Savour Book Vouchers</p>
    <p>and Maple Orchard supplied Discount vouchers.</p>
    <p>Savour Vouchers are eligible only for Dine-In.</p>
  </section>

  <section class="section right byo">
    <h2>BYO</h2>
    <p>BYO allowed – only for Wine .</p>
    <p>Charges per bottle apply</p>
  </section>

  <section class="section right online">
    <h2>Order Online</h2>
    <p>www.mapleorchard.com.au</p>
    <p>www.dishdash.com.au</p>
    <p>www.platego.com.au</p>
    <p>www.streetbite.com.au</p>
  </section>

  <section class="section right facilities">
    <h2>Facilities</h2>
    <p>Wheel chair access</p>
    <p>Disabled Toilet inside</p>
    <p>Baby Changer table</p>
    <p>High rise tables for babies</p>
    <p>Music System</p>
  </section>

  <footer class="alert-band">
    <h3>WARNING</h3>
    <p>Please inform wait staff for any allergies. Food consumed at your own risk.</p>
  </footer>
</main>
</body>
</html>
```